Powerpoint Template Background Design

We are looking to update our powerpoint background to align better with our recently updated logo. I've included our current logo (BankGothic Md BT Medium) and previous ppt background we had used for reference. Page orientation should be landscape. Should be usable online and as a printable deck. We are in the digital advertising sales industry and represent various digital ad products to ad agencies and clients who are interested in marketing their products using mobile advertising tools. the RGB color yellow in our logo is 245, 191,34 #fsbf22. We like to also see the grey and black in our logo included. We'd like it to be similar but new and refreshed from our previous ppt background. I've added our current sales deck for your review and consideration with your design.

Target Market(s)

Advertisers, Ad agencies

Industry/Entity Type

Advertising

Colors
ffc214

Requirements
Must have
• Include Logo. Preferably our 3d logo on the cover page. color scheme should match our logo. Must have cover page and template border page that we will use throughout the entire presentation.
Nice to have
• Full cover page graphic using our 3d logo and allows us to add text in a fixed area of the slide
Should not have
• If recommending full slide color/imagery please note it will be used both online and as a printable deck. Do not include the tagline and/or text from the previously used presentation template.

```html
<!DOCTYPE html>
<html lang="en">
<head>
<meta charset="utf-8">
<title>Northvale Media – Presentation Template</title>
<link href="https://fonts.googleapis.com/css2?family=Open+Sans:wght@400;600;700;800&display=swap" rel="stylesheet">
<style>
:root{
  --board:#d9d9d9;
  --paper:#ffffff;
  --gold:#b38b12;
  --gold-dark:#8c6d10;
  --yellow:#f5bf22;
  --cream:#f6f1e2;
  --grey:#9a9a9a;
  --grey-light:#e6e6e6;
  --ink:#2a2a2a;
}
*{margin:0;padding:0;box-sizing:border-box}
html,body{width:1200px;height:900px;overflow:hidden;background:var(--board);font-family:'Open Sans',Arial,sans-serif;color:var(--ink)}
.board{position:relative;width:1200px;height:900px}
.slide{position:absolute;width:245px;height:138px;background:var(--paper);overflow:hidden;box-shadow:0 1px 3px rgba(0,0,0,.15)}
.abs{position:absolute}
.title{position:absolute;left:0;top:6px;height:8px;border-left:3px solid var(--yellow);padding-left:6px;font-size:5.5px;font-weight:700;line-height:8px;color:var(--ink)}
.footer{position:absolute;left:9px;right:0;bottom:6px;height:6px;display:flex;align-items:center;gap:3px;font-size:3.2px;color:#555}
.footer .dot{width:5px;height:5px;border-radius:50%;background:var(--grey)}
.footer .rule{flex:1;height:.5px;background:#ccc;margin-right:12px}
.pageno{position:absolute;right:0;bottom:4px;width:9px;height:8px;background:var(--yellow);font-size:3.5px;font-weight:700;text-align:center;line-height:8px;color:var(--ink)}
.tx{font-size:3px;line-height:4px;color:#555}
.tx-w{font-size:3.2px;line-height:4.2px;color:#fff}
.lbl{font-size:3.8px;font-weight:700;color:var(--gold)}
.photo{position:absolute}
.ph-warm{background:linear-gradient(135deg,#c9b48a,#8a6a3a 55%,#e9dcc2)}
.ph-office{background:linear-gradient(135deg,#e4dfd6,#9c8f7e 50%,#d8d2c8)}
.ph-blue{background:linear-gradient(135deg,#6d8bb0,#c7d4e4 50%,#3c4f6a)}
.ph-city{background:linear-gradient(135deg,#2d3a4a,#7f93a8 50%,#1f2a36)}
.icon{fill:var(--gold)}
.box{position:absolute;background:#fff;border:.5px solid #e0d7bd;display:flex;flex-direction:column;align-items:center;justify-content:center;gap:3px;font-size:3px;font-weight:600}
.tag{position:absolute;width:35px;height:8px;color:#fff;font-size:3.2px;font-weight:700;text-align:center;line-height:8px}
</style>
</head>
<body>
<div class="board">

<!-- 1 Cover -->
<section class="slide" style="left:72px;top:59px">
  <div class="photo" style="inset:0;background:linear-gradient(120deg,#d6b64a 0%,#a38a4f 40%,#6f6a5c 70%,#c9a63a 100%)" role="img" aria-label="Cover photo of a team working at a desk with a golden overlay"></div>
  <div class="abs" style="left:0;top:0;width:61px;height:37px;background:#fff;display:flex;align-items:center;justify-content:center;gap:2px">
    <span style="width:4px;height:4px;background:var(--yellow);border-radius:50%"></span>
    <span style="font-size:5px;font-weight:800;color:var(--ink)">NORTHVALE</span>
  </div>
  <div class="abs" style="left:155px;top:98px;font-size:9px;font-weight:600;color:#fff">Edit title here</div>
  <div class="abs" style="left:176px;top:110px;font-size:4px;font-weight:600;color:#fff">edit subtitle here</div>
  <div class="abs" style="left:220px;top:95px;width:1px;height:26px;background:#fff"></div>
</section>

<!-- 2 -->
<section class="slide" style="left:342px;top:59px">
  <div class="title">EDIT TITLE HERE</div>
  <div class="abs" style="left:13px;top:30px;width:91px;height:89px;background:var(--gold);padding:10px 12px">
    <p class="tx-w">Lorem ipsum dolor sit amet consectetur adipiscing elit sed do eiusmod tempor incididunt ut labore et dolore magna aliqua ut enim ad minim veniam quis nostrud exercitation ullamco laboris nisi ut aliquip ex ea commodo consequat duis aute irure dolor in reprehenderit in voluptate velit esse cillum dolore eu fugiat nulla pariatur excepteur sint occaecat.</p>
  </div>
  <div class="photo ph-office" style="left:104px;top:30px;width:127px;height:89px" role="img" aria-label="Top view of a meeting table with laptops and documents"></div>
  <div class="footer"><span class="dot"></span>Northvale Media<span class="rule"></span></div><div class="pageno">2</div>
</section>

<!-- 3 Team -->
<section class="slide" style="left:613px;top:59px">
  <div class="title">EDIT TITLE HERE</div>
  <div class="photo" style="left:27px;top:37px;width:34px;height:34px;border-radius:50%;background:#cfcfcf" role="img" aria-label="Portrait of team member"></div>
  <div class="photo" style="left:79px;top:37px;width:34px;height:34px;border-radius:50%;background:#cfcfcf" role="img" aria-label="Portrait of team member"></div>
  <div class="photo" style="left:130px;top:37px;width:34px;height:34px;border-radius:50%;background:#cfcfcf" role="img" aria-label="Portrait of team member"></div>
  <div class="photo" style="left:181px;top:37px;width:34px;height:34px;border-radius:50%;background:#cfcfcf" role="img" aria-label="Portrait of team member"></div>
  <div class="abs lbl" style="left:22px;top:79px;width:44px;text-align:center">CLARA VOSS<div class="tx">General Manager</div></div>
  <div class="abs lbl" style="left:74px;top:79px;width:44px;text-align:center">PETER LUND<div class="tx">Trainer Head</div></div>
  <div class="abs lbl" style="left:125px;top:79px;width:44px;text-align:center">MARCO HALE<div class="tx">Finance</div></div>
  <div class="abs lbl" style="left:176px;top:79px;width:44px;text-align:center">IVAN REYES<div class="tx">Senior Trainer</div></div>
  <p class="abs tx" style="left:20px;top:94px;width:205px">Lorem ipsum dolor sit amet consectetur adipiscing elit sed do eiusmod tempor incididunt ut labore et dolore magna aliqua ut enim ad minim veniam quis nostrud exercitation ullamco laboris nisi ut aliquip ex ea commodo consequat duis aute irure dolor in reprehenderit in voluptate velit esse cillum dolore.</p>
  <div class="footer"><span class="dot"></span>Northvale Media<span class="rule"></span></div><div class="pageno">3</div>
</section>

<!-- 4 -->
<section class="slide" style="left:886px;top:59px">
  <div class="title">EDIT TITLE HERE</div>
  <div class="abs" style="left:0;top:21px;width:139px;height:101px;background:var(--gold)"></div>
  <div class="photo ph-office" style="left:139px;top:21px;width:106px;height:101px" role="img" aria-label="Bright empty office interior"></div>
  <p class="abs tx-w" style="left:22px;top:34px;width:46px;font-weight:700">Lorem ipsum dolor sit amet consectetur adipiscing elit cras ac efficitur ipsum lobortis non praesent vitae pulvinar lorem ipsum dolor sit amet consectetur adipiscing elit cras bibendum mattis leo.</p>
  <div class="abs" style="left:71px;top:42px;width:161px;height:59px;background:#fff;display:flex;justify-content:space-around;align-items:center;font-size:4px;font-weight:700">
    <div style="text-align:center"><svg width="10" height="10" viewBox="0 0 10 10"><rect class="icon" x="0" y="0" width="4" height="4"/><rect class="icon" x="5" y="0" width="4" height="4"/><rect class="icon" x="0" y="5" width="4" height="4"/><rect class="icon" x="5" y="5" width="4" height="4"/></svg><br>LOREM</div>
    <div style="text-align:center"><svg width="10" height="10" viewBox="0 0 10 10"><path class="icon" d="M5 0 10 5H8.5V10H1.5V5H0Z"/></svg><br>LOREM</div>
    <div style="text-align:center"><svg width="10" height="10" viewBox="0 0 10 10"><circle cx="5" cy="5" r="3.5" fill="none" stroke="var(--gold)" stroke-width="2" stroke-dasharray="2 1"/><circle class="icon" cx="5" cy="5" r="1.3"/></svg><br>LOREM</div>
  </div>
  <div class="footer"><span class="dot"></span>Northvale Media<span class="rule"></span></div><div class="pageno">4</div>
</section>

<!-- 5 -->
<section class="slide" style="left:72px;top:218px">
  <div class="title">EDIT TITLE HERE</div>
  <div class="photo ph-warm" style="left:12px;top:25px;width:71px;height:58px" role="img" aria-label="Professional working with colleagues"></div>
  <div class="photo ph-blue" style="left:88px;top:25px;width:71px;height:58px" role="img" aria-label="Doctors reviewing a laptop"></div>
  <div class="photo ph-office" style="left:164px;top:25px;width:71px;height:58px" role="img" aria-label="Hands over charts on a desk"></div>
  <div class="abs" style="left:12px;top:88px;width:71px;text-align:center"><div class="lbl">LOREM IPSUM</div><p class="tx">Lorem ipsum dolor sit amet consectetur adipiscing elit sed do eiusmod tempor incididunt ut labore.</p></div>
  <div class="abs" style="left:88px;top:88px;width:71px;text-align:center"><div class="lbl">LOREM IPSUM</div><p class="tx">Lorem ipsum dolor sit amet consectetur adipiscing elit sed do eiusmod tempor incididunt ut labore.</p></div>
  <div class="abs" style="left:164px;top:88px;width:71px;text-align:center"><div class="lbl">LOREM IPSUM</div><p class="tx">Lorem ipsum dolor sit amet consectetur adipiscing elit sed do eiusmod tempor incididunt ut labore.</p></div>
  <div class="footer"><span class="dot"></span>Northvale Media<span class="rule"></span></div><div class="pageno">5</div>
</section>

<!-- 6 -->
<section class="slide" style="left:342px;top:218px">
  <div class="title">EDIT TITLE HERE</div>
  <div class="photo ph-office" style="left:13px;top:25px;width:88px;height:95px" role="img" aria-label="Man working at a computer in a library office"></div>
  <p class="abs tx" style="left:115px;top:30px;width:118px">Lorem ipsum dolor sit amet consectetur adipiscing elit sed do eiusmod tempor incididunt ut labore et dolore magna aliqua ut enim ad minim veniam quis nostrud exercitation ullamco laboris nisi ut aliquip ex ea commodo consequat duis aute irure dolor in reprehenderit in voluptate velit esse cillum dolore eu fugiat nulla pariatur.</p>
  <div class="abs" style="left:115px;top:82px;width:120px;display:flex;justify-content:space-between;text-align:center">
    <div style="width:36px"><svg width="10" height="10" viewBox="0 0 10 10"><rect class="icon" x="0" y="1" width="10" height="9"/><path d="M5 3 8 6H2Z" fill="#fff"/></svg><p class="tx">Lorem ipsum dolor sit amet elit sed.</p></div>
    <div style="width:36px"><svg width="10" height="10" viewBox="0 0 10 10"><rect class="icon" x="0" y="6" width="2" height="4"/><rect class="icon" x="3" y="4" width="2" height="6"/><rect class="icon" x="6" y="2" width="2" height="8"/><path d="M0 5 4 2 7 3 10 0" stroke="var(--gold)" fill="none" stroke-width=".8"/></svg><p class="tx">Lorem ipsum dolor sit amet elit sed.</p></div>
    <div style="width:36px"><svg width="10" height="10" viewBox="0 0 10 10"><rect class="icon" x="1" y="0" width="8" height="10"/><rect x="2.5" y="2" width="2" height="2" fill="#fff"/><rect x="5.5" y="2" width="2" height="2" fill="#fff"/><rect x="2.5" y="5" width="2" height="2" fill="#fff"/><rect x="5.5" y="5" width="2" height="2" fill="#fff"/></svg><p class="tx">Lorem ipsum dolor sit amet elit sed.</p></div>
  </div>
  <div class="footer"><span class="dot"></span>Northvale Media<span class="rule"></span></div><div class="pageno">6</div>
</section>

<!-- 7 List -->
<section class="slide" style="left:613px;top:218px">
  <div class="title">EDIT TITLE HERE</div>
  <ol class="abs" style="left:28px;top:28px;list-style:none;font-size:4px;font-weight:700">
    <li style="height:14.5px;display:flex;gap:7px"><span style="background:var(--yellow);color:#fff;width:7px;height:7px;text-align:center;line-height:7px">1</span>Lorem ipsum dolor sit amet consectetur adipiscing elit.</li>
    <li style="height:14.5px;display:flex;gap:7px"><span style="background:var(--yellow);color:#fff;width:7px;height:7px;text-align:center;line-height:7px">2</span>Lorem ipsum dolor sit amet consectetur adipiscing elit.</li>
    <li style="height:14.5px;display:flex;gap:7px"><span style="background:var(--yellow);color:#fff;width:7px;height:7px;text-align:center;line-height:7px">3</span>Lorem ipsum dolor sit amet consectetur adipiscing elit.</li>
    <li style="height:14.5px;display:flex;gap:7px"><span style="background:var(--yellow);color:#fff;width:7px;height:7px;text-align:center;line-height:7px">4</span>Lorem ipsum dolor sit amet consectetur adipiscing elit.</li>
    <li style="height:14.5px;display:flex;gap:7px"><span style="background:var(--yellow);color:#fff;width:7px;height:7px;text-align:center;line-height:7px">5</span>Lorem ipsum dolor sit amet consectetur adipiscing elit.</li>
    <li style="height:14.5px;display:flex;gap:7px"><span style="background:var(--yellow);color:#fff;width:7px;height:7px;text-align:center;line-height:7px">6</span>Lorem ipsum dolor sit amet consectetur adipiscing elit.</li>
  </ol>
  <div class="photo ph-office" style="left:160px;top:22px;width:65px;height:98px" role="img" aria-label="Two colleagues reviewing work together"></div>
  <div class="footer"><span class="dot"></span>Northvale Media<span class="rule"></span></div><div class="pageno">7</div>
</section>

<!-- 8 Icon grid -->
<section class="slide" style="left:886px;top:218px">
  <div class="title">EDIT TITLE HERE</div>
  <div class="abs" style="left:0;top:21px;width:245px;height:100px;background:var(--cream)"></div>
  <div class="box" style="left:20px;top:29px;width:50px;height:39px"><svg width="11" height="10" viewBox="0 0 11 10"><rect class="icon" x="4" y="0" width="3" height="3"/><rect class="icon" x="0" y="7" width="3" height="3"/><rect class="icon" x="4" y="7" width="3" height="3"/><rect class="icon" x="8" y="7" width="3" height="3"/><path d="M5.5 3V5M1.5 7V5H9.5V7" stroke="var(--gold)" fill="none" stroke-width=".8"/></svg>LOREM IPSUM</div>
  <div class="box" style="left:73px;top:29px;width:50px;height:39px"><svg width="11" height="10" viewBox="0 0 11 10"><rect x=".5" y=".5" width="10" height="9" fill="none" stroke="var(--gold)"/><path class="icon" d="M1.5 8.5 4.5 4.5 6.5 7 8 5.5 9.5 8.5Z"/></svg>LOREM IPSUM</div>
  <div class="box" style="left:126px;top:29px;width:50px;height:39px"><svg width="11" height="10" viewBox="0 0 11 10"><path class="icon" d="M2 9A2.5 2.5 0 0 1 2 4 3.5 3.5 0 0 1 9 4 2.5 2.5 0 0 1 9 9Z"/><circle cx="5.5" cy="6.5" r="1.3" fill="#fff"/></svg>LOREM IPSUM</div>
  <div class="box" style="left:179px;top:29px;width:50px;height:39px"><svg width="11" height="10" viewBox="0 0 11 10"><circle class="icon" cx="5.5" cy="5" r="5"/><path d="M3 4H8M3 6H8" stroke="#fff" stroke-width=".8"/></svg>LOREM IPSUM</div>
  <div class="box" style="left:20px;top:76px;width:50px;height:38px"><svg width="11" height="10" viewBox="0 0 11 10"><path class="icon" d="M2.5 9A2.5 2.5 0 0 1 2.5 4 3.5 3.5 0 0 1 9 3.5 2.8 2.8 0 0 1 8.5 9Z"/></svg>LOREM IPSUM</div>
  <div class="box" style="left:73px;top:76px;width:50px;height:38px"><svg width="11" height="10" viewBox="0 0 11 10"><rect class="icon" x="0" y="2" width="11" height="8"/><rect x="4" y="0" width="3" height="2" fill="none" stroke="var(--gold)" stroke-width=".8"/><path d="M0 5H11" stroke="#fff" stroke-width=".6"/></svg>LOREM IPSUM</div>
  <div class="box" style="left:126px;top:76px;width:50px;height:38px"><svg width="11" height="10" viewBox="0 0 11 10"><path class="icon" d="M2.5 0H8.5V10L5.5 7 2.5 10Z"/></svg>LOREM IPSUM</div>
  <div class="box" style="left:179px;top:76px;width:50px;height:38px"><svg width="11" height="10" viewBox="0 0 11 10"><path class="icon" d="M5.5 0 11 2.5H0Z"/><rect class="icon" x="1" y="3" width="1.5" height="5"/><rect class="icon" x="4" y="3" width="1.5" height="5"/><rect class="icon" x="7" y="3" width="1.5" height="5"/><rect class="icon" x="0" y="8.5" width="11" height="1.5"/></svg>LOREM IPSUM</div>
  <div class="footer"><span class="dot"></span>Northvale Media<span class="rule"></span></div><div class="pageno">8</div>
</section>

<!-- 9 Mobile -->
<section class="slide" style="left:72px;top:380px">
  <div class="title">EDIT TITLE HERE</div>
  <div class="abs" style="left:103px;top:36px;width:38px;height:72px;background:var(--gold);border-radius:4px;padding:7px 3px 9px">
    <div style="width:100%;height:100%" class="ph-warm" role="img" aria-label="Photo on the phone screen"></div>
  </div>
  <div class="abs" style="left:120px;top:101px;width:4px;height:4px;border-radius:50%;background:#fff"></div>
  <div class="abs" style="left:30px;top:36px;width:68px;text-align:right">
    <div style="height:20px"><div class="lbl" style="font-size:3.4px">Lorem ipsum dolor sit</div><p class="tx">Lorem ipsum dolor sit amet consectetur adipiscing elit sed.</p></div>
    <div style="height:20px"><div class="lbl" style="font-size:3.4px">Lorem ipsum dolor sit</div><p class="tx">Lorem ipsum dolor sit amet consectetur adipiscing elit sed.</p></div>
    <div style="height:20px"><div class="lbl" style="font-size:3.4px">Lorem ipsum dolor sit</div><p class="tx">Lorem ipsum dolor sit amet consectetur adipiscing elit sed.</p></div>
    <div style="height:20px"><div class="lbl" style="font-size:3.4px">Lorem ipsum dolor sit</div><p class="tx">Lorem ipsum dolor sit amet consectetur adipiscing elit sed.</p></div>
  </div>
  <div class="abs" style="left:160px;top:34px;width:70px">
    <div style="height:20px"><div class="lbl" style="font-size:3.4px">Lorem ipsum dolor sit</div><p class="tx">Lorem ipsum dolor sit amet consectetur adipiscing elit sed.</p></div>
    <div style="height:20px"><div class="lbl" style="font-size:3.4px">Lorem ipsum dolor sit</div><p class="tx">Lorem ipsum dolor sit amet consectetur adipiscing elit sed.</p></div>
    <div style="height:20px"><div class="lbl" style="font-size:3.4px">Lorem ipsum dolor sit</div><p class="tx">Lorem ipsum dolor sit amet consectetur adipiscing elit sed.</p></div>
    <div style="height:20px"><div class="lbl" style="font-size:3.4px">Lorem ipsum dolor sit</div><p class="tx">Lorem ipsum dolor sit amet consectetur adipiscing elit sed.</p></div>
  </div>
  <div class="footer"><span class="dot"></span>Northvale Media<span class="rule"></span></div><div class="pageno">9</div>
</section>

<!-- 10 -->
<section class="slide" style="left:342px;top:380px">
  <div class="title">EDIT TITLE HERE</div>
  <div class="abs" style="left:15px;top:21px;font-size:3.6px;font-weight:600">Lorem ipsum dolor sit amet, consectetur adipiscing elit. Aenean sed tempor lorem. Suspendisse</div>
  <div class="photo ph-blue" style="left:15px;top:30px;width:215px;height:51px" role="img" aria-label="Business people shaking hands in silhouette against a city skyline"></div>
  <div class="abs" style="left:15px;top:83px;width:215px;display:flex;gap:5px">
    <div style="flex:1"><div style="background:var(--gold);color:#fff;font-size:3.4px;font-weight:700;text-align:center;height:9px;line-height:9px">Lorem ipsum dolor</div><p class="tx" style="text-align:center;margin-top:3px">Lorem ipsum dolor sit amet consectetur adipiscing elit sed tempor.</p></div>
    <div style="flex:1"><div style="background:var(--yellow);color:#fff;font-size:3.4px;font-weight:700;text-align:center;height:9px;line-height:9px">Lorem ipsum dolor</div><p class="tx" style="text-align:center;margin-top:3px">Lorem ipsum dolor sit amet consectetur adipiscing elit sed tempor.</p></div>
    <div style="flex:1"><div style="background:var(--gold);color:#fff;font-size:3.4px;font-weight:700;text-align:center;height:9px;line-height:9px">Lorem ipsum dolor</div><p class="tx" style="text-align:center;margin-top:3px">Lorem ipsum dolor sit amet consectetur adipiscing elit sed tempor.</p></div>
    <div style="flex:1"><div style="background:var(--yellow);color:#fff;font-size:3.4px;font-weight:700;text-align:center;height:9px;line-height:9px">Lorem ipsum dolor</div><p class="tx" style="text-align:center;margin-top:3px">Lorem ipsum dolor sit amet consectetur adipiscing elit sed tempor.</p></div>
  </div>
  <div class="footer"><span class="dot"></span>Northvale Media<span class="rule"></span></div><div class="pageno">10</div>
</section>

<!-- 11 Table -->
<section class="slide" style="left:613px;top:380px">
  <div class="title">EDIT TITLE HERE</div>
  <p class="abs tx" style="left:17px;top:24px;width:211px">Lorem ipsum dolor sit amet consectetur adipiscing elit sed do eiusmod tempor incididunt ut labore et dolore magna aliqua ut enim ad minim veniam quis nostrud exercitation ullamco laboris nisi ut aliquip.</p>
  <table class="abs" style="left:17px;top:45px;width:211px;border-collapse:collapse;font-size:3.6px;font-weight:600;text-align:center">
    <tr style="height:11px;color:#fff"><td style="background:var(--gold)">Lorem</td><td style="background:var(--yellow)">Lorem</td><td style="background:var(--gold)">Lorem</td><td style="background:var(--yellow)">Lorem</td></tr>
    <tr style="height:12px;background:var(--grey-light)"><td>Lorem</td><td>Lorem</td><td>Lorem</td><td>Lorem</td></tr>
    <tr style="height:12px;background:#f4f4f4"><td>Lorem</td><td>Lorem</td><td>Lorem</td><td>Lorem</td></tr>
    <tr style="height:12px;background:var(--grey-light)"><td>Lorem</td><td>Lorem</td><td>Lorem</td><td>Lorem</td></tr>
    <tr style="height:12px;background:#f4f4f4"><td>Lorem</td><td>Lorem</td><td>Lorem</td><td>Lorem</td></tr>
    <tr style="height:11px;background:var(--grey-light)"><td>Lorem</td><td>Lorem</td><td>Lorem</td><td>Lorem</td></tr>
  </table>
  <div class="footer"><span class="dot"></span>Northvale Media<span class="rule"></span></div><div class="pageno">11</div>
</section>

<!-- 12 -->
<section class="slide" style="left:886px;top:380px">
  <div class="title">EDIT TITLE HERE</div>
  <p class="abs tx" style="left:40px;top:24px;width:195px">Lorem ipsum dolor sit amet consectetur adipiscing elit sed do eiusmod tempor incididunt ut labore et dolore magna aliqua ut enim ad minim veniam.</p>
  <div class="abs" style="left:0;top:38px;width:245px;height:71px;background:var(--gold)"></div>
  <div class="photo" style="left:12px;top:30px;width:70px;height:66px;background:linear-gradient(160deg,#f2f2f2,#bdbdbd 60%,#e2e2e2)" role="img" aria-label="Desktop computer monitor"></div>
  <div class="abs" style="left:98px;top:55px;width:140px;display:flex;justify-content:space-between;text-align:center">
    <div style="width:32px"><svg width="12" height="12" viewBox="0 0 12 12"><circle cx="6" cy="6" r="5.3" fill="none" stroke="#fff" stroke-width=".8"/><path d="M3.5 6 5.3 7.8 8.5 4.3" stroke="#fff" fill="none"/></svg><p class="tx-w">Lorem ipsum dolor sit</p></div>
    <div style="width:32px"><svg width="12" height="12" viewBox="0 0 12 12"><circle cx="6" cy="6" r="5.3" fill="none" stroke="#fff" stroke-width=".8"/><path d="M3 8 5 6 6.5 7 9 4" stroke="#fff" fill="none"/></svg><p class="tx-w">Lorem ipsum dolor sit</p></div>
    <div style="width:32px"><svg width="12" height="12" viewBox="0 0 12 12"><circle cx="6" cy="6" r="5.3" fill="none" stroke="#fff" stroke-width=".8"/><rect x="3.3" y="4" width="5.4" height="3.5" fill="none" stroke="#fff" stroke-width=".7"/></svg><p class="tx-w">Lorem ipsum dolor sit</p></div>
    <div style="width:32px"><svg width="12" height="12" viewBox="0 0 12 12"><circle cx="6" cy="6" r="5.3" fill="none" stroke="#fff" stroke-width=".8"/><path d="M6 3V7M4 5 6 3 8 5M3.5 8.5H8.5" stroke="#fff" fill="none" stroke-width=".8"/></svg><p class="tx-w">Lorem ipsum dolor sit</p></div>
  </div>
  <p class="abs tx" style="left:40px;top:112px;width:195px">Lorem ipsum dolor sit amet consectetur adipiscing elit sed do eiusmod tempor incididunt ut labore et dolore magna.</p>
  <div class="footer"><span class="dot"></span>Northvale Media<span class="rule"></span></div><div class="pageno">12</div>
</section>

<!-- 13 -->
<section class="slide" style="left:72px;top:541px">
  <div class="title">EDIT TITLE HERE</div>
  <div class="abs" style="left:0;top:24px;width:98px;height:96px;background:var(--cream)"></div>
  <p class="abs tx" style="left:10px;top:30px;width:82px">Lorem ipsum dolor sit amet consectetur adipiscing elit sed do eiusmod tempor incididunt ut labore et dolore magna aliqua ut enim ad minim veniam quis nostrud exercitation ullamco laboris nisi ut aliquip ex ea commodo consequat duis aute irure dolor in reprehenderit in voluptate velit esse cillum dolore eu fugiat nulla pariatur excepteur sint occaecat cupidatat non proident sunt in culpa qui officia deserunt mollit anim id est laborum sed ut perspiciatis.</p>
  <div class="abs" style="left:98px;top:24px;width:147px;height:96px;background:linear-gradient(120deg,var(--gold),#c9a54a)"></div>
  <div class="abs" style="left:98px;top:36px;width:147px;text-align:center;font-size:6.5px;font-weight:700;color:#fff">Lorem ipsum dolor sit amet</div>
  <div class="abs" style="left:110px;top:54px;width:125px;display:grid;grid-template-columns:repeat(3,1fr);gap:6px 8px">
    <div style="border:.6px solid #fff;height:16px" class="tx-w"><p style="text-align:center;padding-top:4px">Lorem ipsum dolor sit amet</p></div>
    <div style="border:.6px solid #fff;height:16px" class="tx-w"><p style="text-align:center;padding-top:4px">Lorem ipsum dolor sit amet</p></div>
    <div style="border:.6px solid #fff;height:16px" class="tx-w"><p style="text-align:center;padding-top:4px">Lorem ipsum dolor sit amet</p></div>
    <div style="border:.6px solid #fff;height:16px" class="tx-w"><p style="text-align:center;padding-top:4px">Lorem ipsum dolor sit amet</p></div>
    <div style="border:.6px solid #fff;height:16px" class="tx-w"><p style="text-align:center;padding-top:4px">Lorem ipsum dolor sit amet</p></div>
    <div style="border:.6px solid #fff;height:16px" class="tx-w"><p style="text-align:center;padding-top:4px">Lorem ipsum dolor sit amet</p></div>
  </div>
  <div class="footer"><span class="dot"></span>Northvale Media<span class="rule"></span></div><div class="pageno">13</div>
</section>

<!-- 14 Org chart -->
<section class="slide" style="left:342px;top:541px">
  <div class="title">EDIT TITLE HERE</div>
  <svg class="abs" style="left:0;top:0" width="245" height="138" viewBox="0 0 245 138">
    <g stroke="#bbb" stroke-width=".6" fill="none">
      <path d="M118 37V46M55 46H182M55 46V53M98 46V53M142 46V53M182 46V53"/>
      <path d="M98 61V71M142 61V71M98 79V88M142 79V88"/>
      <path d="M48 61V90H98M190 61V90H142M48 75V99H98M190 75V99H142M98 88V96M142 88V96"/>
    </g>
  </svg>
  <div class="tag" style="left:101px;top:28px;height:9px;line-height:9px;background:var(--gold)">LOREM IPSUM</div>
  <div class="tag" style="left:37px;top:53px;background:var(--gold)">LOREM IPSUM</div>
  <div class="tag" style="left:81px;top:53px;background:var(--yellow)">LOREM IPSUM</div>
  <div class="tag" style="left:125px;top:53px;background:var(--yellow)">LOREM IPSUM</div>
  <div class="tag" style="left:169px;top:53px;background:var(--gold)">LOREM IPSUM</div>
  <div class="tag" style="left:81px;top:71px;background:var(--yellow)">LOREM IPSUM</div>
  <div class="tag" style="left:125px;top:71px;background:var(--yellow)">LOREM IPSUM</div>
  <div class="tag" style="left:81px;top:88px;background:var(--yellow)">LOREM IPSUM</div>
  <div class="tag" style="left:125px;top:88px;background:var(--yellow)">LOREM IPSUM</div>
  <p class="abs tx" style="left:15px;top:104px;width:215px">Lorem ipsum dolor sit amet consectetur adipiscing elit sed do eiusmod tempor incididunt ut labore et dolore magna aliqua ut enim ad minim veniam quis nostrud exercitation ullamco laboris nisi ut aliquip ex ea commodo consequat.</p>
  <div class="footer"><span class="dot"></span>Northvale Media<span class="rule"></span></div><div class="pageno">14</div>
</section>

<!-- 15 Map -->
<section class="slide" style="left:613px;top:541px">
  <div class="title">EDIT TITLE HERE</div>
  <div class="photo" style="left:28px;top:24px;width:192px;height:68px;background:linear-gradient(180deg,#c4c4c4,#a9a9a9)" role="img" aria-label="Grey world map with yellow and gold location markers"></div>
  <div class="abs" style="left:16px;top:98px;font-size:3.6px;font-weight:700;display:flex;align-items:center;gap:4px"><span style="width:7px;height:7px;border-radius:50%;background:var(--yellow)"></span>EDIT TITLE HERE</div>
  <div class="abs" style="left:16px;top:112px;font-size:3.6px;font-weight:700;display:flex;align-items:center;gap:4px"><span style="width:7px;height:7px;border-radius:50%;background:var(--gold)"></span>EDIT TITLE HERE</div>
  <div class="footer"><span class="dot"></span>Northvale Media<span class="rule"></span></div><div class="pageno">15</div>
</section>

<!-- 16 -->
<section class="slide" style="left:886px;top:541px">
  <div class="title">EDIT TITLE HERE</div>
  <div class="photo ph-city" style="left:0;top:25px;width:245px;height:96px" role="img" aria-label="City at night with connected light trails"></div>
  <div class="abs" style="left:22px;top:25px;width:89px;height:96px;background:var(--gold);padding:13px 8px">
    <div style="font-size:6px;font-weight:700;color:#fff;margin-bottom:3px">LOREM IPSUM</div>
    <p class="tx-w">Lorem ipsum dolor sit amet consectetur adipiscing elit sed do eiusmod tempor incididunt ut labore et dolore magna aliqua ut enim ad minim veniam quis nostrud exercitation ullamco laboris nisi ut aliquip ex ea commodo consequat duis aute irure dolor.</p>
  </div>
  <div class="footer"><span class="dot"></span>Northvale Media<span class="rule"></span></div><div class="pageno">16</div>
</section>

<!-- 17 Thank you -->
<section class="slide" style="left:342px;top:704px">
  <div class="photo" style="inset:0;background:linear-gradient(120deg,#b6982f 0%,#8d7a45 45%,#6c7a85 70%,#d2b85a 100%)" role="img" aria-label="Group of smiling people holding speech bubbles"></div>
  <div class="abs" style="left:45px;top:65px;font-size:10px;font-weight:600;color:#fff">THANK <b style="font-weight:800">YOU</b></div>
</section>

<!-- 18 Contact -->
<section class="slide" style="left:618px;top:704px">
  <div class="abs" style="left:0;top:10px;width:2px;height:9px;background:var(--yellow)"></div>
  <div class="abs" style="left:15px;top:11px;font-size:6.5px;font-weight:600">Contact us</div>
  <div class="abs" style="left:15px;top:37px;width:60px"><div class="lbl" style="font-size:3.4px">United States</div><p class="tx">Lorem ipsum dolor sit amet consectetur adipiscing elit phone number here.</p></div>
  <div class="abs" style="left:15px;top:67px;width:60px"><div class="lbl" style="font-size:3.4px">Europe</div><p class="tx">Lorem ipsum dolor sit amet consectetur adipiscing elit phone number here.</p></div>
  <div class="abs" style="left:15px;top:96px;display:flex;align-items:center;gap:2px"><span style="width:4px;height:4px;background:var(--yellow);border-radius:50%"></span><span style="font-size:5px;font-weight:800">NORTHVALE</span></div>
  <p class="abs tx" style="left:15px;top:112px;width:130px;font-size:2.6px;line-height:3.2px">Lorem ipsum dolor sit amet consectetur adipiscing elit sed do eiusmod tempor incididunt ut labore et dolore magna aliqua ut enim ad minim veniam quis nostrud.</p>
  <svg class="abs" style="left:0;top:0" width="245" height="138" viewBox="0 0 245 138" role="img" aria-label="City skyline with connected network icons">
    <defs><linearGradient id="sky" x1="0" y1="0" x2="1" y2="1"><stop offset="0" stop-color="#6f8ea6"/><stop offset=".5" stop-color="#c9c7a9"/><stop offset="1" stop-color="#7e8f6a"/></linearGradient></defs>
    <path d="M115 0H245V138H170Z" fill="url(#sky)"/>
    <path d="M245 60V138H150Z" fill="var(--yellow)" opacity=".95"/>
  </svg>
  <div class="abs" style="right:16px;bottom:10px;font-size:3.4px;font-weight:700;color:#fff">www.northvalemedia.com</div>
</section>

</div>
</body>
</html>
```